RWT Installations Ltd Business Cards

We need a business card with our business logo. We provide window and door installations on high-rises in west coast British Colombia, Canada.

I would like my business information and details on one side of the card, and the other side the company name with logo

Target Market(s)

General Contractors

Industry/Entity Type

Construction

Contact Information for Business Card

one side i want my company name and logo in the dark theme logo that i provided

Requirements
Must have
• Tomas Verelund, 15559284016, RWTInstallations@mailvera.example, 1408-5192 Pellow Avenue Burnaby BC, V0X 1Z9, Owner & Manager

```html
<!DOCTYPE html>
<html lang="en">
<head>
<meta charset="utf-8">
<title>RWT Installations Ltd — Business Cards</title>
<link href="https://fonts.googleapis.com/css2?family=Montserrat:wght@300;400;500;600&display=swap" rel="stylesheet">
<style>
  :root {
    --page-bg: #e9eaeb;
    --card-dark: #2c2c2d;
    --card-mid: #3a3a3b;
    --facade-dark: #232427;
    --facade-steel: #4a5561;
    --facade-light: #7d8a98;
    --brand-blue: #2ea3dc;
    --text-light: #f2f2f2;
    --text-soft: #c9c9c9;
    --text-muted: #8c8c8c;
  }
  * { margin: 0; padding: 0; box-sizing: border-box; }
  html, body {
    width: 1200px; height: 900px; overflow: hidden;
    background: var(--page-bg);
    font-family: "Montserrat", sans-serif;
  }
  .sheet {
    width: 1200px; height: 900px;
    display: flex; flex-direction: column;
    align-items: center; justify-content: center; gap: 40px;
  }
  .card {
    position: relative;
    width: 700px; height: 400px;
    background: var(--card-dark);
    overflow: hidden;
    box-shadow: 0 8px 24px rgba(0,0,0,0.18);
  }

  /* Front */
  .card-front { background: var(--card-mid); }
  .card-front .facade {
    position: absolute; top: 0; right: 0; bottom: 0; width: 64%;
    background: linear-gradient(160deg, var(--facade-dark) 0%, #2f3134 55%, #34373b 100%);
  }
  .brand {
    position: absolute; left: 150px; top: 150px;
    display: flex; flex-direction: column; gap: 18px;
  }
  .brand-mark {
    display: flex; align-items: center; gap: 16px;
  }
  .brand-square {
    width: 46px; height: 46px; background: var(--brand-blue);
  }
  .brand-name {
    font-size: 38px; font-weight: 600; color: var(--brand-blue);
    letter-spacing: 0.5px; line-height: 1;
  }
  .brand-legal {
    margin-left: 62px;
    font-size: 11px; font-weight: 400; letter-spacing: 1.5px;
    color: var(--text-muted); text-transform: uppercase;
  }

  /* Back */
  .card-back .facade {
    position: absolute; top: 0; right: 0; bottom: 0; width: 58%;
    background:
      radial-gradient(ellipse at 70% 45%, rgba(160,175,192,0.55) 0%, rgba(160,175,192,0) 45%),
      linear-gradient(90deg, var(--card-dark) 0%, var(--facade-steel) 45%, var(--facade-light) 75%, var(--facade-steel) 100%);
  }
  .person {
    position: absolute; left: 50px; top: 48px;
  }
  .person-name {
    font-size: 36px; font-weight: 400; color: var(--text-light); letter-spacing: 0.5px;
  }
  .person-role {
    margin-top: 8px;
    font-size: 16px; font-weight: 400; color: var(--text-soft);
  }
  .contact-list {
    position: absolute; left: 50px; bottom: 38px;
    list-style: none; display: flex; flex-direction: column; gap: 9px;
  }
  .contact-item {
    display: flex; align-items: center; gap: 14px;
    font-size: 12.5px; font-weight: 400; color: var(--text-light);
  }
  .contact-icon { width: 12px; height: 12px; flex: none; fill: var(--text-light); }
</style>
</head>
<body>
<main class="sheet">

  <section class="card card-front" aria-label="Business card front">
    <div class="facade" role="img" aria-label="Photograph of a dark glass high-rise facade"></div>
    <div class="brand">
      <div class="brand-mark">
        <span class="brand-square"></span>
        <span class="brand-name">RWT Installations Ltd</span>
      </div>
      <span class="brand-legal">RWT Installations Ltd.</span>
    </div>
  </section>

  <section class="card card-back" aria-label="Business card back">
    <div class="facade" role="img" aria-label="Photograph of a glass high-rise facade reflecting cloudy sky"></div>
    <div class="person">
      <h1 class="person-name">Tomas Verelund</h1>
      <p class="person-role">Owner &amp; Manager</p>
    </div>
    <ul class="contact-list">
      <li class="contact-item">
        <svg class="contact-icon" viewBox="0 0 12 12" aria-hidden="true"><path d="M2 1h2.5l1 3-1.5 1c.6 1.3 1.7 2.4 3 3l1-1.5 3 1V10c0 .6-.4 1-1 1C5 11 1 7 1 2c0-.6.4-1 1-1z"/></svg>
        <span>15559284016</span>
      </li>
      <li class="contact-item">
        <svg class="contact-icon" viewBox="0 0 12 12" aria-hidden="true"><path d="M1 2.5h10v7H1z M1.5 3l4.5 3.5L10.5 3" fill="none" stroke="#f2f2f2" stroke-width="1.2"/></svg>
        <span>RWTInstallations@mailvera.example</span>
      </li>
      <li class="contact-item">
        <svg class="contact-icon" viewBox="0 0 12 12" aria-hidden="true"><path d="M6 0.8C3.9 0.8 2.3 2.4 2.3 4.5 2.3 7.3 6 11.2 6 11.2s3.7-3.9 3.7-6.7C9.7 2.4 8.1.8 6 .8zm0 5.1a1.5 1.5 0 110-3 1.5 1.5 0 010 3z"/></svg>
        <span>1408-5192 Pellow Avenue Burnaby BC, V0X 1Z9</span>
      </li>
      <li class="contact-item">
        <svg class="contact-icon" viewBox="0 0 12 12" aria-hidden="true"><circle cx="6" cy="6" r="5"/></svg>
        <span>@RWTINSTALLATIONSLTD</span>
      </li>
    </ul>
  </section>

</main>
</body>
</html>
```